QUORVIX - Sydney Based Technology Consultancy -Logo & Business Card design

Who are we?
-
Quorvix is an emerging and advanced technology consulting and professional services business based in Sydney, Australia. Quorvix specialising in increasing value to organisations through the effective use of current and emerging technologies, ensuring that technology is a sustainable catalyst to attaining stated business goals.

We pride ourselves in challenging the norm.

What do we want?
-
We are looking to update our "Brand" we already have a simple “home grown” logo and we are now looking for a new one, once we have this updated logo and businesses look and feel though the business card design we will refresh our website with the new logo and design thus updating the Companies overall look at feel.

Our current site is www.quorvix-example.net.au is a very basic wordpress site and we will be updating it once we have the new logo and designs done

Our initial thoughts on the new Quorvix identity are
• Logo Concept
- One of the key things is obviously the 8
- I was thinking that a logo that had 8 as the core of the logo would be cool,
- Almost like having a “ring” or hoop that is twisted to form an 8 with different services scribed on the inside.
- So we would have a Large 8 and the inside would have ring each service or section engraved.

• Brand / web Feel
- Simple
- Professional
- Innovative
- Clear
- Destination
- Unique
- Impartial
- Safe
- Leading edge
- Familiar

- Emerging technologies
- White and ice / glacier blue
- The familiar feel of the Brindle web site
- Embedded specialist Video clips

• Portfolio of Services
- Quorvix – A smart place for Smart people
- Quorvix – we provide the process to take ideas from awareness to reality
- Focus should be on the brand quality consistent clear local knowledge with regional, national, theatre and global presence

Access to Specialists
- Emerging technologies
- Sustainability
- Collaboration
- Data centre
- Virtualisation

• Adjacent ideas under the one Brand
- Tembrosk – Enable Business Collaboration
- Plinsk – Infrastructure Virtualisation
- morvo - smart people and processes
- skandel - Emerging technologies
- brunhavel - business to technology integration
- tolpin - Smart Infrastructure
- yusk – Connected communities
- dwol - sustainability

Target Market(s)

Australia, New Zealand and Asia pacific organisations that are typically English speaking.
Markets
- IT & Technology partners
- Banking and Finance
- Health

Industry/Entity Type

Business

Requirements
Must have
• Logo
Business cards
Colour pallette
3D Logo
Nice to have
• Style guide
Designer who can also assist with new Wordpress design
Should not have
• we don't want cheap looking, overtly flashy or gimmicky logo.

```html
<!DOCTYPE html>
<html lang="en">
<head>
<meta charset="utf-8">
<title>Quorvix Business Card</title>
<link rel="stylesheet" href="https://fonts.googleapis.com/css2?family=Michroma&family=Montserrat:ital,wght@0,400;0,500;1,400&family=Press+Start+2P&display=swap">
<style>
  :root {
    --page: #ffffff;
    --strip-dark: #1c120c;
    --strip-mid: #3a2a20;
    --band-light: #ffffff;
    --band-mid: #e6e6e6;
    --band-low: #b9b9b9;
    --brand-grey: #4a4a4a;
    --card-black: #111111;
    --card-black-top: #2b2b2b;
    --text-white: #ffffff;
    --text-soft: #d8d8d8;
  }
  html, body {
    margin: 0;
    padding: 0;
    width: 1200px;
    height: 719px;
    overflow: hidden;
    background: var(--page);
  }
  .canvas {
    position: relative;
    width: 1200px;
    height: 719px;
  }
  .card {
    position: absolute;
    left: 90px;
    top: 114px;
    width: 1068px;
    height: 552px;
    border-radius: 48px;
    overflow: hidden;
    background: var(--card-black);
    box-shadow: 0 4px 14px rgba(0,0,0,0.25);
  }
  .card__strip {
    position: absolute;
    left: 0; top: 0;
    width: 100%;
    height: 40px;
    background: linear-gradient(to bottom, var(--strip-dark), var(--strip-mid));
  }
  .card__band {
    position: absolute;
    left: 0; top: 40px;
    width: 100%;
    height: 256px;
    background: linear-gradient(to bottom, var(--band-light) 0%, var(--band-mid) 55%, var(--band-low) 100%);
  }
  .card__lower {
    position: absolute;
    left: 0; top: 296px;
    width: 100%;
    height: 256px;
    background: linear-gradient(to bottom, var(--card-black-top) 0%, var(--card-black) 35%, var(--card-black) 100%);
  }
  .brand-name {
    position: absolute;
    left: 0; top: 130px;
    width: 100%;
    text-align: center;
    margin: 0;
    font-family: "Michroma", sans-serif;
    font-size: 84px;
    font-weight: 400;
    letter-spacing: 3px;
    line-height: 1;
    color: var(--brand-grey);
  }
  .holder-name {
    position: absolute;
    left: 51px; top: 344px;
    margin: 0;
    font-family: "Montserrat", sans-serif;
    font-weight: 500;
    font-size: 38px;
    letter-spacing: 2px;
    color: var(--text-white);
  }
  .holder-role {
    position: absolute;
    left: 180px; top: 396px;
    margin: 0;
    font-family: "Montserrat", sans-serif;
    font-style: italic;
    font-size: 13px;
    letter-spacing: 1.5px;
    color: var(--text-soft);
  }
  .contact {
    position: absolute;
    left: 81px; top: 480px;
    margin: 0;
    font-family: "Montserrat", sans-serif;
    font-size: 15px;
    line-height: 26px;
    color: var(--text-white);
  }
  .contact__label {
    display: inline-block;
    width: 168px;
  }
  .contact__sep {
    margin-right: 10px;
  }
  .side-info {
    position: absolute;
    right: 64px; top: 468px;
    margin: 0;
    font-family: "Press Start 2P", monospace;
    font-size: 13px;
    line-height: 24px;
    color: var(--text-white);
  }
</style>
</head>
<body>
<div class="canvas">
  <article class="card">
    <div class="card__strip"></div>
    <div class="card__band">
      <h1 class="brand-name">QUORVIX</h1>
    </div>
    <div class="card__lower"></div>

    <h2 class="holder-name">DARREN KELT MOSSARO</h2>
    <p class="holder-role">JOB DESCRIPTION</p>

    <p class="contact">
      <span class="contact__label">Mobile Number <span class="contact__sep">:</span></span>+61 400 555 019<br>
      <span class="contact__label">Email Address <span class="contact__sep">:</span></span>darrenmossaro@quorvix.test
    </p>

    <p class="side-info">
      002-5870-31<br>
      555-210-8839<br>
      quorvix.test
    </p>
  </article>
</div>
</body>
</html>
```